Global lighting company needs compelling e-tail graphic

Our company is a global lighting company that sells light bulbs, lighting fixtures and ceiling fans. For this project, we have a concept developed for a graphic that explains color temperature for LED light bulbs. We would like to develop this concept into something more exciting and polished for consumer-friendly use on our e-tail product pages.Color temperature, in simple terms, is the ambience and atmosphere created by the color of a light bulb. More detailed information about color temperature can be found here: http://www.brantmoorlamps.com/color-temperature.aspx

Target Market(s)

Online consumers, homeowners

Industry/Entity Type

Lighting Fixture

Font styles to use
Sans Serif

Colors

Designer to choose colors to be used in the design.

Requirements
Must have
• Images depicting color temperature, preferably residential room scenes

```html
<!DOCTYPE html>
<html lang="en">
<head>
<meta charset="utf-8">
<title>Color Temperature Guide</title>
<link rel="stylesheet" href="https://fonts.googleapis.com/css2?family=Fira+Sans:wght@500;600&display=swap">
<style>
  :root {
    --ink: #262626;
    --paper: #ffffff;
    --warm-red: #f47f6f;
    --warm-orange: #fdc566;
    --soft-yellow: #fff39c;
    --neutral-white: #fffff6;
    --cool-blue: #8ed2f3;
  }
  html, body {
    margin: 0;
    padding: 0;
    overflow: hidden;
    background: var(--paper);
  }
  .guide {
    position: relative;
    width: 1200px;
    height: 680px;
    overflow: hidden;
    background: var(--paper);
    font-family: "Fira Sans", sans-serif;
    color: var(--ink);
  }
  .guide-art {
    position: absolute;
    inset: 0;
    width: 1200px;
    height: 680px;
  }
  .guide-title {
    position: absolute;
    top: 66px;
    left: 0;
    width: 1200px;
    margin: 0;
    text-align: center;
    font-size: 35px;
    font-weight: 500;
    letter-spacing: 0.1px;
  }
  .mood-label,
  .kelvin-label {
    position: absolute;
    width: 400px;
    margin: 0;
    text-align: center;
  }
  .mood-label {
    top: 157px;
    font-size: 29px;
    font-weight: 500;
  }
  .kelvin-label {
    top: 570px;
    font-size: 23px;
    font-weight: 600;
  }
  .is-warm { left: 66px; }
  .is-neutral { left: 400px; }
  .is-cool { left: 734px; }
</style>
</head>
<body>
<main class="guide">
  <svg class="guide-art" viewBox="0 0 1500 850" aria-hidden="false">
    <defs>
      <linearGradient id="spectrum" x1="82" y1="0" x2="1418" y2="0" gradientUnits="userSpaceOnUse">
        <stop offset="0" stop-color="var(--warm-red)"/>
        <stop offset="0.09" stop-color="var(--warm-red)"/>
        <stop offset="0.25" stop-color="var(--warm-orange)"/>
        <stop offset="0.45" stop-color="var(--soft-yellow)"/>
        <stop offset="0.68" stop-color="var(--neutral-white)"/>
        <stop offset="0.72" stop-color="var(--neutral-white)"/>
        <stop offset="0.84" stop-color="var(--cool-blue)"/>
        <stop offset="1" stop-color="var(--cool-blue)"/>
      </linearGradient>
      <radialGradient id="room-warm" cx="0.35" cy="0.35" r="0.8">
        <stop offset="0" stop-color="#d8c3a5"/>
        <stop offset="0.55" stop-color="#8f7a63"/>
        <stop offset="1" stop-color="#4a3b30"/>
      </radialGradient>
      <radialGradient id="room-neutral" cx="0.35" cy="0.35" r="0.8">
        <stop offset="0" stop-color="#cbc2b8"/>
        <stop offset="0.55" stop-color="#8a8178"/>
        <stop offset="1" stop-color="#45403c"/>
      </radialGradient>
      <radialGradient id="room-cool" cx="0.35" cy="0.35" r="0.8">
        <stop offset="0" stop-color="#c3c7c4"/>
        <stop offset="0.55" stop-color="#818683"/>
        <stop offset="1" stop-color="#3d4242"/>
      </radialGradient>
    </defs>

    <rect class="spectrum-panel" x="82" y="163" width="1336" height="600" rx="62" fill="url(#spectrum)"/>

    <g class="bulb-shapes" fill="var(--paper)">
      <path d="M113 520 C143 620 193 690 208 763 L458 763 C473 690 523 620 553 520 A225 225 0 1 0 113 520 Z"/>
      <path d="M530 520 C560 620 610 690 625 763 L875 763 C890 690 940 620 970 520 A225 225 0 1 0 530 520 Z"/>
      <path d="M947 520 C977 620 1027 690 1042 763 L1292 763 C1307 690 1357 620 1387 520 A225 225 0 1 0 947 520 Z"/>
    </g>

    <circle class="room-scene" cx="333" cy="475" r="205" fill="url(#room-warm)" role="img" aria-label="Living room with table lamp, potted succulent and blue cushion on a sofa, lit with warm 2700K to 3000K light"/>
    <circle class="room-scene" cx="750" cy="475" r="205" fill="url(#room-neutral)" role="img" aria-label="The same living room corner lit with neutral 4000K light"/>
    <circle class="room-scene" cx="1167" cy="475" r="205" fill="url(#room-cool)" role="img" aria-label="The same living room corner lit with cool 5000K daylight"/>
  </svg>

  <h1 class="guide-title">Color temperature affects the mood and ambience of a room</h1>

  <p class="mood-label is-warm">Cozy, Calm, Inviting</p>
  <p class="mood-label is-neutral">Bright, Vibrant</p>
  <p class="mood-label is-cool">Crisp, Invigorating</p>

  <p class="kelvin-label is-warm">2700K - 3000K</p>
  <p class="kelvin-label is-neutral">4000K</p>
  <p class="kelvin-label is-cool">5000K</p>
</main>
</body>
</html>
```